Design eines Notizblocks für Holzverarbeitungsbetrieb
Zielgruppe
Wir sind ein Holzverarbeitungsbetrieb (Tischlerei / Zimmerei).
Wir haben einen Bodenständigen und gehobenen Kundenkreis.
Aufgabenstellung
das Design soll für einen Notizblock fein kariert sein.
Das Logo + Adresse + Telefonnummer + email (+ Dienstleistungen). Logofarbe ist Gelb-grün.
Adresse: Matthias Brandner Gasse 7, 4817 Almhofen; Telefonnummer: +3916 8051 email: office@wendrasch.co.at
(Dienstleistungen: Zimmerei, Bautischler, Möbeltischler, Brandschutz, Fenster, Fassaden;)

```html
<!DOCTYPE html>
<html lang="de">
<head>
<meta charset="utf-8">
<title>Notizblock – Wendrasch</title>
<link href="https://fonts.googleapis.com/css2?family=Open+Sans:wght@400;600&display=swap" rel="stylesheet">
<style>
  :root{
    --bg:#eeeeee;
    --paper:#ffffff;
    --grid:#a9d3ee;
    --grid-soft:#d3e8f6;
    --ink:#55594f;
    --brand:#4f564a;
    --label:#8a8a8a;
    --rule:#c2d8e6;
  }
  html,body{margin:0;padding:0;overflow:hidden;}
  body{width:1200px;height:675px;background:var(--bg);display:flex;align-items:center;justify-content:center;font-family:"Open Sans",sans-serif;}
  .sheet{position:relative;width:450px;height:640px;background:var(--paper);box-shadow:0 2px 10px rgba(0,0,0,.08);}

  .brand{position:absolute;top:52px;left:40px;width:230px;display:flex;align-items:center;justify-content:center;gap:8px;}
  .brand-dot{width:10px;height:10px;border-radius:50%;background:var(--brand);flex:none;}
  .brand-name{font-size:20px;font-weight:600;color:var(--brand);line-height:1;}

  .grid-top{position:absolute;top:20px;left:330px;width:100px;height:100px;
    background-image:linear-gradient(var(--grid-soft) 1px,transparent 1px),linear-gradient(90deg,var(--grid-soft) 1px,transparent 1px);
    background-size:16.75px 16.75px;}

  .field{position:absolute;font-size:8px;color:var(--label);display:flex;align-items:flex-end;}
  .field-line{flex:1;border-bottom:1px dashed var(--rule);margin-left:4px;height:8px;}
  .field--date{top:52px;left:280px;width:44px;}
  .field--project{top:122px;left:20px;width:410px;}

  .grid{position:absolute;top:136px;left:28px;width:402px;height:450px;
    background-image:linear-gradient(var(--grid) 1px,transparent 1px),linear-gradient(90deg,var(--grid) 1px,transparent 1px);
    background-size:16.75px 16.75px;border-right:1px solid var(--grid);border-bottom:1px solid var(--grid);}

  .footer{position:absolute;bottom:16px;left:20px;right:20px;text-align:center;font-size:8.4px;color:var(--ink);line-height:1.5;}
</style>
</head>
<body>
  <main class="sheet">
    <div class="grid-top"></div>
    <header class="brand">
      <span class="brand-dot"></span>
      <span class="brand-name">Wendrasch</span>
    </header>
    <div class="field field--date">Datum:<span class="field-line"></span></div>
    <div class="field field--project">Projekt:<span class="field-line"></span></div>
    <div class="grid"></div>
    <footer class="footer">
      <div>Matthias Brandner Gasse 7, 4817 Almhofen; Telefonnummer: +3916 8051 email: office@wendrasch.co.at</div>
      <div>Unsere Leistungen: Zimmerei, Bautischler, Möbeltischler, Brandschutz, Fenster, Fassaden.</div>
    </footer>
  </main>
</body>
</html>
```